Professional Business Cards for Recruiting Company

We'd like professional 2-sided business cards that reflect a color scheme that matches our website, www.quillmerbay.com, and / or logo that is attached.

Slogan used is "We Find Talent", but needs to be editable because we change it up to "We Know Developers", "We Speak Geek", etc.

Must includes logo, slogan, first and last name, address, email, mobile number and website address.

Files attached for ideas.

Thanks!

Contact Information for Business Card

Logo, Company name, First name, Last name, addresss, email, phone, website address.

Font styles to use
Sans Serif

Colors
0054AA
0677BA
7BADD7
CADEEF
E8F1F8

Requirements
Nice to have
• I do like the following designs. 22962062 and 22962651. Couple ideas anyway.

```html
<!DOCTYPE html>
<html lang="en">
<head>
<meta charset="utf-8">
<title>Quillmer Bay — Business Card</title>
<link rel="stylesheet" href="https://fonts.googleapis.com/css2?family=Montserrat:wght@300;400;500;600;700&display=swap">
<style>
  :root {
    --brand-blue: #114a85;
    --ink-grey: #5a5a5a;
    --rule-grey: #7a7a7a;
    --paper: #ffffff;
    --backdrop: #e6e7e9;
  }
  * { box-sizing: border-box; margin: 0; padding: 0; }
  html, body { width: 1200px; height: 1063px; overflow: hidden; }
  body {
    background: var(--backdrop);
    font-family: "Montserrat", Arial, sans-serif;
    position: relative;
  }
  .card {
    position: absolute;
    left: 298px;
    width: 600px;
    height: 343px;
    box-shadow: 0 6px 18px rgba(0,0,0,0.18);
  }
  .card-front { top: 188px; background: var(--paper); }
  .card-back { top: 581px; background: var(--brand-blue); color: #fff; }

  /* front: brand block */
  .brand { position: absolute; left: 318px; top: 48px; width: 242px; }
  .brand-line { display: flex; align-items: center; gap: 10px; }
  .brand-square { width: 22px; height: 22px; background: var(--brand-blue); flex: none; }
  .brand-name {
    font-weight: 300; font-size: 25px; color: var(--brand-blue);
    letter-spacing: 0.5px; white-space: nowrap;
  }
  .brand-tagline {
    margin-top: 6px; margin-left: 32px;
    font-size: 6.6px; font-weight: 700; letter-spacing: 1.1px;
    color: var(--ink-grey); white-space: nowrap;
  }

  /* front: person */
  .person { position: absolute; left: 42px; top: 168px; }
  .person-name { font-size: 22px; letter-spacing: 0.5px; color: var(--ink-grey); font-weight: 400; }
  .person-name .first { color: var(--brand-blue); font-weight: 600; }
  .person-title { font-size: 14px; color: var(--ink-grey); margin-top: 1px; }

  .divider { position: absolute; left: 42px; top: 223px; width: 518px; height: 4px; }

  .contacts { position: absolute; left: 42px; top: 238px; list-style: none; }
  .contacts li {
    display: flex; align-items: center; gap: 6px;
    height: 17px; margin-bottom: 6.5px;
    font-size: 13px; color: var(--ink-grey); letter-spacing: 0.2px;
  }
  .icon { width: 17px; height: 17px; flex: none; }

  .address {
    position: absolute; right: 40px; top: 237px;
    display: flex; gap: 6px; align-items: flex-start;
  }
  .address p { text-align: right; font-size: 13px; line-height: 19px; color: var(--ink-grey); }
  .address .icon { margin-top: 3px; }

  /* back */
  .back-brand {
    position: absolute; left: 0; right: 0; top: 150px;
    display: flex; justify-content: center; align-items: center; gap: 12px;
  }
  .back-square { width: 30px; height: 30px; background: #fff; }
  .back-name { font-size: 34px; font-weight: 600; letter-spacing: 1px; }
  .slogan {
    position: absolute; left: 0; right: 0; top: 270px;
    display: flex; align-items: center; gap: 10px;
  }
  .slogan::before, .slogan::after { content: ""; flex: 1; height: 1px; background: #fff; }
  .slogan span { font-size: 16px; letter-spacing: 1.2px; font-weight: 400; }
</style>
</head>
<body>
  <section class="card card-front">
    <div class="brand">
      <div class="brand-line">
        <span class="brand-square"></span>
        <span class="brand-name">QUILLMER BAY</span>
      </div>
      <div class="brand-tagline">TALENT SEARCH AND STAFFING PARTNERS</div>
    </div>

    <div class="person">
      <div class="person-name"><span class="first">DANA</span> WHITLOW</div>
      <div class="person-title">CEO/Owner</div>
    </div>

    <svg class="divider" viewBox="0 0 518 4" aria-hidden="true">
      <line x1="150" y1="2.5" x2="518" y2="2.5" stroke="var(--rule-grey)" stroke-width="1"/>
      <polygon points="0,0 150,0 152,4 0,4" fill="var(--brand-blue)"/>
    </svg>

    <ul class="contacts">
      <li>
        <svg class="icon" viewBox="0 0 17 17" aria-hidden="true">
          <rect width="17" height="17" rx="2" fill="var(--brand-blue)"/>
          <path d="M5 3.5l2 0.3 0.8 2.4-1.3 1a6 6 0 0 0 3.3 3.3l1-1.3 2.4.8.3 2c-.3.7-1 1-1.8 1A8.5 8.5 0 0 1 4 5.3c0-.8.3-1.5 1-1.8z" fill="#fff"/>
        </svg>
        555-318-0472
      </li>
      <li>
        <svg class="icon" viewBox="0 0 17 17" aria-hidden="true">
          <rect width="17" height="17" rx="2" fill="var(--brand-blue)"/>
          <rect x="3" y="4.5" width="11" height="8" fill="none" stroke="#fff" stroke-width="1.2"/>
          <path d="M3 4.5l5.5 4.5 5.5-4.5M3 12.5l4-3.5M14 12.5l-4-3.5" fill="none" stroke="#fff" stroke-width="1"/>
        </svg>
        info@quillmerbay.com
      </li>
      <li>
        <svg class="icon" viewBox="0 0 17 17" aria-hidden="true">
          <rect width="17" height="17" rx="2" fill="var(--brand-blue)"/>
          <path d="M5.5 3.5v9.5l2.4-2.3 1.7 3.6 1.4-.7-1.7-3.5 3.3-.2z" fill="#fff"/>
        </svg>
        www.quillmerbay.com
      </li>
    </ul>

    <div class="address">
      <p>48, Harbor Crest Road, Linden<br>city, lane 40219</p>
      <svg class="icon" viewBox="0 0 17 17" aria-hidden="true">
        <rect width="17" height="17" rx="2" fill="var(--brand-blue)"/>
        <path d="M8.5 3.5l5.5 5h-1.7v4.5H10V10H7v3H4.7V8.5H3z" fill="#fff"/>
      </svg>
    </div>
  </section>

  <section class="card card-back">
    <div class="back-brand">
      <span class="back-square"></span>
      <span class="back-name">QUILLMER BAY</span>
    </div>
    <div class="slogan"><span>WE FIND TALENT</span></div>
  </section>
</body>
</html>
```